Custom Home Builder Brochure
Marcus Hollery Construction LLC
Custom Home Builder Brochure - Construction
Creative Brief
Construction
Potential clients for building a new, custom home.
- Calm colors, nothing too bold - Easy to read font - Use the slogan "You Dream It. We'll Build It." with the font that is close to or matches our logo - Include all text that was given in the "details" section of this form.
marcushollerybuilds marcushollerybuilds
I am not sure what a vector file is, please advise. Thank you.
MegaPixelNomad MegaPixelNomad
Dear Project holder, I would be pleased if you could send me the vector file of your logo. Thanks

```html
<!DOCTYPE html>
<html lang="en">
<head>
<meta charset="utf-8">
<title>Marcus Hollery Construction LLC – Brochure</title>
<link href="https://fonts.googleapis.com/css2?family=Open+Sans:ital,wght@0,400;0,600;0,700;1,400&family=Playfair+Display:ital,wght@0,700;1,700&family=Great+Vibes&display=swap" rel="stylesheet">
<style>
  :root{
    --navy:#1e3b66;
    --teal:#22918b;
    --teal-light:#39b2a6;
    --paper:#ffffff;
    --backdrop:#e9e9ea;
    --ink:#4a4f57;
    --quote-bg:#eef0f2;
    --photo-stone:#8a7560;
    --photo-sky:#9fc1dc;
    --photo-grass:#6f8f4b;
    --photo-interior:#a8855f;
  }
  *{box-sizing:border-box;margin:0;padding:0}
  html,body{width:1200px;height:1020px;overflow:hidden;background:var(--backdrop)}
  body{font-family:"Open Sans",sans-serif;color:var(--ink);font-size:8.6px;line-height:1.45}
  .spread{position:absolute;left:30px;width:1140px;height:480px;display:grid;grid-template-columns:repeat(3,1fr);background:var(--paper);box-shadow:0 2px 10px rgba(0,0,0,.15)}
  .spread--outside{top:20px}
  .spread--inside{top:520px}
  .panel{position:relative;overflow:hidden;padding:26px 26px 0;border-right:1px solid #e3e3e3}
  .panel:last-child{border-right:none}
  h2{font-family:"Playfair Display",serif;font-style:italic;font-weight:700;color:var(--navy);font-size:21px;line-height:1.1;margin-bottom:8px}
  p{margin-bottom:7px}
  .photo{display:block;border-radius:2px}
  .photo--house{background:linear-gradient(180deg,var(--photo-sky) 0%,var(--photo-sky) 35%,var(--photo-stone) 36%,#6f5c49 78%,var(--photo-grass) 79%)}
  .photo--interior{background:linear-gradient(135deg,#c9a77c,var(--photo-interior) 55%,#6b4f34)}
  .photo--portrait{background:linear-gradient(180deg,#c9ccd2,#8e949c)}
  .quote{background:var(--quote-bg);border-left:3px solid var(--teal);padding:9px 11px;font-style:italic;font-size:8.4px}
  .quote cite{display:block;text-align:right;font-weight:600;color:var(--navy);margin-top:4px}
  .band{position:absolute;left:0;right:0;bottom:0;background:var(--teal);color:#fff}
  .script{font-family:"Great Vibes",cursive;color:var(--teal);font-weight:400}
  .corner{position:absolute;top:0;left:0;width:18px;height:18px;background:var(--navy)}

  /* outside – intro */
  .intro .band{height:40px;background:linear-gradient(90deg,var(--navy),var(--teal))}
  .intro .quote{margin-top:10px}

  /* outside – back / contact */
  .contact{padding:18px 20px 0}
  .photo-row{display:grid;grid-template-columns:1fr 1fr;gap:6px;margin-bottom:10px}
  .photo-row .photo{height:74px}
  .contact .callout{background:var(--navy);color:#fff;font-style:italic;padding:10px 12px;margin-bottom:12px;font-size:8.4px}
  .contact .callout cite{display:block;text-align:right;color:#bfe3df;margin-top:4px}
  .team{display:grid;grid-template-columns:58px 1fr;gap:8px 10px;align-items:center;margin-bottom:8px}
  .team .photo{height:58px}
  .team strong{display:block;color:var(--navy);font-size:9.4px}
  .contact .band{height:64px;padding:11px 18px;text-align:center;font-size:9px;line-height:1.6}
  .contact .band .web{font-weight:700;font-size:10px}

  /* outside – cover */
  .cover{padding:0;background:var(--paper);display:flex;flex-direction:column;align-items:center}
  .brand{margin-top:22px;display:flex;align-items:center;gap:8px;border:1px solid var(--navy);padding:7px 14px}
  .brand__square{width:14px;height:14px;background:var(--navy)}
  .brand__name{font-family:"Playfair Display",serif;font-weight:700;color:var(--navy);font-size:15px;line-height:1.1;text-align:center}
  .cover .script{font-size:26px;margin:12px 0 8px;line-height:1}
  .cover .photo--house{width:100%;height:210px}
  .cover .tagline{width:100%;background:linear-gradient(90deg,var(--teal),var(--navy));color:#fff;text-align:right;padding:12px 24px;font-size:19px;line-height:1.15}
  .cover .tagline b{display:block;font-family:"Playfair Display",serif;font-size:34px}
  .cover .web{margin-top:14px;color:var(--navy);font-weight:700;font-size:10px}

  /* inside */
  .honest .photo--house{height:150px;margin:8px 0 10px}
  .honest .signature{font-style:italic;text-align:right;color:var(--navy);font-weight:600}
  .quality .photo-grid{display:grid;grid-template-columns:1fr 1fr;gap:5px;margin:6px 0 12px}
  .quality .photo-grid .photo{height:60px}
  .quality .detail{display:grid;grid-template-columns:1fr 110px;gap:10px}
  .quality .detail .photo{height:110px}
  .service .script{font-size:22px;text-align:right;margin:4px 0 8px}
  .service .photo--interior{height:112px}
  .service .band{height:74px;padding:12px 24px;font-style:italic;font-size:8.6px}
</style>
</head>
<body>

<section class="spread spread--outside">
  <article class="panel intro">
    <span class="corner"></span>
    <h2>Introduction</h2>
    <p>It is with great pride that we present this guide to our family business. For over twenty years Marcus Hollery Construction has helped families across the valley turn plans and dreams into homes built to last for generations.</p>
    <p>Our team works side by side with you from the first sketch to the final walk through. We listen closely, explain every choice, and keep you informed so there are never surprises along the way.</p>
    <p>We believe a home is more than walls and a roof. It is where memories are made, where children grow and where friends gather. That is why we treat each project as if it were our very own home.</p>
    <div class="quote">"We were so thrilled with our new home. Every detail was handled with care and the whole crew made us feel like family from day one."<cite>Tom and Ella Varney</cite></div>
    <div class="band"></div>
  </article>

  <article class="panel contact">
    <div class="photo-row">
      <span class="photo photo--house" role="img" aria-label="Photo of a finished stone home exterior"></span>
      <span class="photo photo--house" role="img" aria-label="Photo of a brick home with landscaped yard"></span>
    </div>
    <div class="callout">"Our goal has always been simple: build homes we would be proud to live in, and treat every client with honesty and respect."<cite>Marcus Hollery</cite></div>
    <div class="team">
      <span class="photo photo--portrait" role="img" aria-label="Portrait of Marcus Hollery"></span>
      <div><strong>Marcus Hollery</strong>Owner / Builder<br>(555) 014-2290</div>
      <span class="photo photo--portrait" role="img" aria-label="Portrait of Anna Hollery"></span>
      <div><strong>Anna Hollery</strong>Design Consultant<br>(555) 014-2291</div>
    </div>
    <div class="band">
      Marcus Hollery Construction LLC<br>
      418 Larkspur Road, Cedar Falls · (555) 014-2290<br>
      <span class="web">www.marcushollerybuilds.com</span>
    </div>
  </article>

  <article class="panel cover">
    <div class="brand">
      <span class="brand__square"></span>
      <span class="brand__name">Marcus Hollery<br>Construction LLC</span>
    </div>
    <div class="script">You Dream It. We'll Build It.</div>
    <span class="photo photo--house" role="img" aria-label="Large photo of a stone custom home with arched windows and green lawn"></span>
    <div class="tagline">Building<br>Quality Homes<br>with <b>Integrity</b></div>
    <div class="web">www.marcushollerybuilds.com</div>
  </article>
</section>

<section class="spread spread--inside">
  <article class="panel honest">
    <h2>An Honest Builder</h2>
    <p>Marcus Hollery Construction is a locally owned builder devoted to the people of Cedar Falls. Our clients trust us because we keep our word, stick to our budgets and stand behind every home we build. We never cut corners.</p>
    <p>From the first meeting we give clear prices and honest timelines. If something changes, you will hear it from us first, along with the options available to you.</p>
    <span class="photo photo--house" role="img" aria-label="Photo of a brick home with a front porch at dusk"></span>
    <p>"Choosing Marcus was the best decision we made. He was open with us at every step and our home is even better than we pictured."</p>
    <p class="signature">Ruth and Dean Calloway</p>
  </article>

  <article class="panel quality">
    <h2>Quality Construction</h2>
    <p>We use only trusted materials and skilled craftsmen. Each stage is checked with care so your home is solid, safe and built to last.</p>
    <div class="photo-grid">
      <span class="photo photo--interior" role="img" aria-label="Photo of a bright kitchen interior"></span>
      <span class="photo photo--interior" role="img" aria-label="Photo of a living room with fireplace"></span>
      <span class="photo photo--interior" role="img" aria-label="Photo of a master bathroom"></span>
      <span class="photo photo--interior" role="img" aria-label="Photo of a dining room"></span>
    </div>
    <h2>Attention To Detail</h2>
    <div class="detail">
      <p>Small touches make a house feel like home. From trim work to cabinet hardware, we take time over every finish and welcome your ideas so the result reflects your style and the way you live.</p>
      <span class="photo photo--interior" role="img" aria-label="Photo of detailed trim and staircase"></span>
    </div>
  </article>

  <article class="panel service">
    <h2>Customer Service</h2>
    <p>Building a home should be exciting, not stressful. We return calls promptly, meet with you on site and walk you through each milestone so you always know where things stand.</p>
    <p>Our care does not end at closing. We follow up after you move in and remain here for any questions in the years ahead.</p>
    <div class="script">We look forward to meeting you!</div>
    <span class="photo photo--interior" role="img" aria-label="Photo of a finished family room interior"></span>
    <div class="band">"Marcus and his team answered every question and finished on time. We could not be happier with our new home." — Tom and Ella Varney</div>
  </article>
</section>

</body>
</html>
```